harbor mental health stationary

Please help turn this logo into a total image for my business.
Stationary need to be able to be individualized for each mental health practitioners

Some generic info about services
Clinical Psychology - Consultant Psychiatry - Locum Services - Medico-legal - Architectural Adviser Clinical and Medical Facilities

Target Market(s)

Letter head for doctors, courts, patients.

Industry/Entity Type

Mental Health

Requirements
Must have
• area where practitioners details can be listed and logo on page
Nice to have
• embossed section

```html
<!DOCTYPE html>
<html lang="en">
<head>
<meta charset="utf-8">
<title>Harbor Mental Health – Envelope</title>
<link href="https://fonts.googleapis.com/css2?family=Arimo:wght@400&display=swap" rel="stylesheet">
<style>
  :root {
    --backdrop: #d5d5d5;
    --paper: #ffffff;
    --navy: #12476a;
    --teal: #0a87ad;
    --ink: #4a4a4a;
    --rule: #bdbdbd;
  }
  html, body {
    margin: 0;
    padding: 0;
    width: 1200px;
    height: 1000px;
    overflow: hidden;
    background: var(--backdrop);
    font-family: "Arimo", Arial, sans-serif;
  }
  .canvas { position: relative; width: 1200px; height: 1000px; }
  .envelope-back, .envelope-front {
    position: absolute;
    left: 60px;
    width: 1075px;
    height: 466px;
    background: var(--paper);
  }
  .envelope-back { top: 23px; }
  .envelope-back svg { display: block; }
  .envelope-front { top: 519px; box-shadow: 0 0 0 1px #e3e3e3; }

  .brand { position: absolute; left: 24px; top: 16px; display: flex; align-items: flex-start; }
  .brand-mark { width: 69px; height: 69px; background: var(--teal); }
  .brand-name {
    margin-left: 14px;
    color: var(--navy);
    font-weight: 400;
    text-transform: uppercase;
    line-height: 1;
  }
  .brand-name .primary { display: block; font-size: 44px; letter-spacing: 0.5px; margin-top: 2px; }
  .brand-name .secondary { display: block; font-size: 21px; letter-spacing: 0.6px; margin-top: 2px; }

  .practitioner { position: absolute; left: 24px; top: 360px; }
  .practitioner .name { color: var(--teal); font-size: 18px; margin: 0 0 6px; }
  .practitioner .line { color: var(--ink); font-size: 15.5px; margin: 0 0 4px; }

  .divider {
    position: absolute; left: 244px; top: 360px; width: 2px; height: 82px;
    background: linear-gradient(to bottom, rgba(10,135,173,0), var(--teal) 50%, rgba(10,135,173,0));
  }

  .contact { position: absolute; left: 270px; top: 360px; font-size: 12px; color: var(--ink); }
  .contact-row { display: flex; align-items: center; height: 16.5px; }
  .contact-row svg { width: 11px; height: 11px; margin-right: 5px; fill: var(--navy); }
  .registration { position: absolute; left: 258px; top: 426px; font-size: 11.5px; color: var(--ink); }
  .registration .label { color: var(--teal); }
  .registration .gap { display: inline-block; width: 18px; }
  .website { position: absolute; left: 258px; top: 440px; font-size: 11px; color: var(--teal); }
</style>
</head>
<body>
<div class="canvas">

  <section class="envelope-back" aria-label="Envelope back">
    <svg width="1075" height="466" viewBox="0 0 1075 466">
      <rect x="0.5" y="0.5" width="1074" height="465" fill="none" stroke="var(--rule)"/>
      <line x1="44" y1="57" x2="44" y2="400" stroke="var(--rule)"/>
      <line x1="1031" y1="57" x2="1031" y2="400" stroke="var(--rule)"/>
      <path d="M0,466 L40,420 Q60,390 110,387 H965 Q1015,390 1035,420 L1075,466" fill="none" stroke="var(--rule)"/>
      <path class="flap" d="M0,0 H1075 V20 Q1070,68 1030,75 L690,178 Q610,199 537,199 Q465,199 385,178 L45,75 Q5,68 0,20 Z" fill="var(--navy)"/>
      <rect class="flap-mark" x="504" y="75" width="68" height="68" rx="2" fill="var(--teal)"/>
    </svg>
  </section>

  <section class="envelope-front" aria-label="Envelope front">
    <div class="brand">
      <div class="brand-mark"></div>
      <div class="brand-name">
        <span class="primary">Harbor</span>
        <span class="secondary">Mental Health</span>
      </div>
    </div>

    <div class="practitioner">
      <p class="name">Doctor’s Name</p>
      <p class="line">Qualifications</p>
      <p class="line">Description</p>
    </div>

    <div class="divider"></div>

    <div class="contact">
      <div class="contact-row">
        <svg viewBox="0 0 12 12"><path d="M6 0a4 4 0 0 0-4 4c0 3 4 8 4 8s4-5 4-8a4 4 0 0 0-4-4zm0 5.6A1.6 1.6 0 1 1 6 2.4a1.6 1.6 0 0 1 0 3.2z"/></svg>
        <span>24 Marlow Street, BAYVIEW 6021</span>
      </div>
      <div class="contact-row">
        <svg viewBox="0 0 12 12"><path d="M2.4 0.5l2 2.2-1 1.4c.8 1.7 2 2.9 3.6 3.7l1.4-1 2.2 2-1.2 2C5 10.6 1.3 7 0.5 1.7z"/></svg>
        <span>(08) 5550 1234 or 0400555210</span>
      </div>
      <div class="contact-row">
        <svg viewBox="0 0 12 12"><path d="M3 0h6v12H3zM4 1.5v8h4v-8zM5.4 10.2h1.2v1H5.4z"/></svg>
        <span>+000 000 0000</span>
      </div>
      <div class="contact-row">
        <svg viewBox="0 0 12 12"><path d="M0 2.5h12v7H0zm1 1v.4l5 3 5-3v-.4z"/></svg>
        <span>name@hmh.net.au</span>
      </div>
    </div>

    <div class="registration">
      <span class="label">ABN:</span>00 123 456 789<span class="gap"></span><span class="label">ACN:</span>000123456
    </div>
    <div class="website">www.harbormentalhealth.com</div>
  </section>

</div>
</body>
</html>
```